Iron Pivot Hoops Academy- Small Group and Private Lessons

I would like to advertise and drive my small group basketball lessons (offered on Fridays during the summer in Prosper, Texas with the following four groups- 1. Middle School Girls Small Group, 2. Middle School Boys Small Group, 3. High School Girls Small Group, 4. High School Boys Small Group).
Tag Line- "Do you want to become a complete player?"
We work to make each player as well rounded as possible by focusing on: balanced footwork, ballhandling, dribbling, finishing, passing, shooting, moving without the ball, basketball IQ
Website- www.ironpivothoopsacademy.com

```html
<!DOCTYPE html>
<html lang="en">
<head>
<meta charset="utf-8">
<title>Iron Pivot Hoops Academy – Small Group Lessons</title>
<link href="https://fonts.googleapis.com/css2?family=Roboto+Condensed:ital,wght@0,400;0,700;1,700&family=Roboto:wght@500;700&display=swap" rel="stylesheet">
<style>
  :root {
    --orange: #f7931e;
    --orange-deep: #e8801a;
    --charcoal: #3a3a3a;
    --ink: #333333;
    --white: #ffffff;
    --paper: #fbfbfb;
    --stage: #5b5b5b;
    --silhouette-a: #4a4a4a;
    --silhouette-b: #6a6a6a;
  }
  * { margin: 0; padding: 0; box-sizing: border-box; }
  html, body { width: 1027px; height: 1200px; overflow: hidden; }
  body { background: var(--stage); position: relative; font-family: "Roboto Condensed", "Arial Narrow", sans-serif; }

  .flyer {
    position: absolute; left: 115px; top: 20px;
    width: 796px; height: 1160px;
    background: var(--paper);
    overflow: hidden;
  }
  .flyer__decor { position: absolute; inset: 0; }

  .headline { position: absolute; left: 56px; top: 40px; color: var(--white); font-weight: 700; text-transform: uppercase; line-height: 0.95; z-index: 2; }
  .headline__small { font-size: 32px; display: block; }
  .headline__want { font-size: 76px; display: block; }
  .headline__become { font-size: 34px; display: block; margin-top: 2px; }
  .headline__become b { font-size: 42px; }
  .headline__complete { font-size: 70px; display: block; margin-top: 26px; font-weight: 400; }
  .headline__player { font-size: 88px; display: block; font-weight: 400; }
  .invite { position: absolute; left: 56px; top: 400px; color: var(--white); font-size: 25px; font-weight: 700; line-height: 1.35; z-index: 2; }
  .invite em { font-style: italic; }

  .skills { position: absolute; right: 110px; top: 44px; list-style: none; text-align: right; font-family: "Roboto", sans-serif; font-weight: 500; font-size: 26px; line-height: 37px; color: var(--ink); z-index: 2; }

  .figure { position: absolute; border-radius: 40px; background: linear-gradient(160deg, var(--silhouette-b), var(--silhouette-a)); opacity: 0.9; }
  .figure--drive { left: 395px; top: 40px; width: 130px; height: 330px; }
  .figure--layup { left: 690px; top: 290px; width: 100px; height: 190px; }
  .figure--crossover { left: 585px; top: 360px; width: 150px; height: 270px; }
  .figure--handle { left: 640px; top: 720px; width: 120px; height: 180px; }

  .ball { position: absolute; border-radius: 50%; background: radial-gradient(circle at 35% 35%, #ffb04a, var(--orange-deep)); }
  .ball--small { left: 170px; top: 960px; width: 84px; height: 84px; }
  .ball--large { left: 600px; top: 892px; width: 136px; height: 136px; }

  .brand { position: absolute; left: 292px; top: 428px; width: 264px; height: 264px; border-radius: 50%; background: var(--white); box-shadow: 0 0 0 10px rgba(255,255,255,0.6); display: flex; align-items: center; justify-content: center; text-align: center; z-index: 1; }
  .brand__name { font-size: 40px; font-weight: 700; text-transform: uppercase; color: var(--charcoal); line-height: 1.05; }

  .location { position: absolute; left: 92px; top: 510px; color: var(--ink); font-size: 30px; font-weight: 700; text-transform: uppercase; line-height: 1.15; text-align: center; width: 130px; }
  .location svg { display: block; margin: 0 auto 14px; }

  .lessons-badge { position: absolute; left: 65px; top: 762px; width: 168px; height: 168px; border-radius: 50%; background: var(--orange); box-shadow: 0 0 0 8px var(--white); color: var(--white); text-align: center; display: flex; flex-direction: column; justify-content: center; font-weight: 700; }
  .lessons-badge__title { font-size: 28px; line-height: 1.1; text-transform: uppercase; }
  .lessons-badge__rule { height: 2px; background: var(--white); margin: 8px 12px; }
  .lessons-badge__sub { font-size: 22px; }

  .groups { position: absolute; left: 320px; top: 780px; list-style: none; z-index: 2; }
  .groups li { height: 62px; }
  .groups__name { display: block; font-size: 27px; font-weight: 700; color: var(--ink); text-transform: uppercase; line-height: 1.05; }
  .groups__tag { display: block; font-size: 19px; font-weight: 700; color: var(--orange); padding-left: 27px; text-transform: uppercase; }

  .web-bar { position: absolute; left: 28px; top: 1062px; width: 690px; height: 50px; background: var(--charcoal); display: flex; align-items: center; padding-left: 22px; }
  .web-bar__url { font-family: "Roboto", sans-serif; font-weight: 700; font-size: 31px; color: var(--white); letter-spacing: -0.3px; }
  .web-bar__url span { color: var(--orange); }
  .web-bar__chevrons { position: absolute; right: -50px; top: 0; }
</style>
</head>
<body>
  <main class="flyer">
    <svg class="flyer__decor" width="796" height="1160" viewBox="0 0 796 1160" aria-hidden="true">
      <g fill="none" stroke="#ececec" stroke-width="6">
        <path d="M470 240 Q600 420 470 640"/>
        <path d="M420 620 Q200 820 60 1150"/>
        <path d="M620 560 Q790 700 796 900"/>
      </g>
      <polygon points="0,0 477,0 418,418 0,544" fill="var(--orange)"/>
      <g fill="none" stroke="var(--charcoal)" stroke-width="2.5" stroke-dasharray="9 7">
        <path d="M700 10 Q820 200 660 360"/>
        <path d="M560 330 Q640 280 700 300"/>
        <path d="M200 690 Q230 740 270 770 Q285 785 298 792"/>
        <path d="M70 880 Q20 960 150 980"/>
        <path d="M765 430 Q735 600 780 800"/>
        <path d="M765 850 Q772 950 736 980"/>
      </g>
      <path d="M292 792 l14 6 l-10 8 z" fill="var(--charcoal)"/>
      <g stroke="var(--orange)" stroke-width="2.5" stroke-dasharray="7 5">
        <line x1="700" y1="80" x2="790" y2="80"/>
        <line x1="700" y1="118" x2="790" y2="118"/>
        <line x1="700" y1="156" x2="790" y2="156"/>
        <line x1="700" y1="194" x2="790" y2="194"/>
        <line x1="700" y1="232" x2="790" y2="232"/>
      </g>
    </svg>

    <div class="figure figure--drive" role="img" aria-label="Silhouette of a player driving with the ball"></div>
    <div class="figure figure--layup" role="img" aria-label="Silhouette of a player going up for a layup"></div>
    <div class="figure figure--crossover" role="img" aria-label="Silhouette of a girl dribbling a crossover"></div>
    <div class="figure figure--handle" role="img" aria-label="Silhouette of a girl dribbling low"></div>

    <h1 class="headline">
      <span class="headline__small">Do you</span>
      <span class="headline__want">Want</span>
      <span class="headline__become">to <b>become</b> a</span>
      <span class="headline__complete">Complete</span>
      <span class="headline__player">Player</span>
    </h1>
    <p class="invite">Join Our <em>Small Groups</em><br>on <em>Fridays</em> during<br>the <em>summer</em></p>

    <ul class="skills">
      <li>footwork</li><li>ballhandling</li><li>dribbling</li><li>finishing</li><li>passing</li><li>shooting</li><li>basketball IQ</li>
    </ul>

    <div class="location">
      <svg width="34" height="46" viewBox="0 0 34 46" aria-hidden="true"><path d="M17 2a15 15 0 0 1 15 15c0 11-15 27-15 27S2 28 2 17A15 15 0 0 1 17 2z" fill="var(--charcoal)"/><circle cx="17" cy="17" r="6" fill="var(--paper)"/></svg>
      Prosper<br>Texas
    </div>

    <div class="brand"><span class="brand__name">Iron Pivot<br>Hoops<br>Academy</span></div>

    <div class="lessons-badge">
      <span class="lessons-badge__title">Small<br>Group<br>Lessons</span>
      <span class="lessons-badge__rule"></span>
      <span class="lessons-badge__sub">Every Friday</span>
    </div>

    <ol class="groups">
      <li><span class="groups__name">1. Middle School Girls</span><span class="groups__tag">Small Group</span></li>
      <li><span class="groups__name">2. Middle School Boys</span><span class="groups__tag">Small Group</span></li>
      <li><span class="groups__name">3. High School Girls</span><span class="groups__tag">Small Group</span></li>
      <li><span class="groups__name">4. High School Boys</span><span class="groups__tag">Small Group</span></li>
    </ol>

    <div class="ball ball--small" role="img" aria-label="Basketball"></div>
    <div class="ball ball--large" role="img" aria-label="Basketball"></div>

    <div class="web-bar">
      <span class="web-bar__url">www.<span>iron</span>pivot<span>hoops</span>academy<span>.com</span></span>
      <svg class="web-bar__chevrons" width="50" height="50" viewBox="0 0 50 50" aria-hidden="true">
        <g fill="var(--charcoal)"><path d="M0 0h10l14 25-14 25H0l14-25z"/><path d="M18 0h10l14 25-14 25H18l14-25z"/></g>
      </svg>
    </div>
  </main>
</body>
</html>
```